Advertising poster for a small Antenna business A3 in size

G,day my name is marcel .. im 30 years of age and i have only had my business for 5 months , the business is clean neat and professional and prides its self on results and quality customer service .
the business will be targeting ages of 20-80 years of age in a country town that is rapidly expanding .
I need a poster that speaks to the customer showing what I do and a friendly customer service .. preferably some sort of antenna installation on a roof and myself helping a customer in a family room environment to give that friendly vibe , need clean sleek photos eg plasma tv hung on a wall of a new contemporary home , well dressed customers and a professional looking installer and what ever else your creative mind imagination can come up with .

business name is " Marcels Antenna Service "
Phone number is 0491 32 60 47
services we provide
.new home antenna installations
.repair your dodgy reception
.wall mount your big screen TV's
.add extra outlets
.supply and install low cost security camera setups
.TELVIQ satellite installations
.anything tv related ,call marcel , he can do it !

please add the above text to the poster so that the customer knows what we do

The business's catchy phrase is "call marcel , he can do it "
provided will be just a photo of the van I drive .. I don't mind if the van is not in the poster .. but at least you will get an idea of whats going on, colors ect ect
I want to draw the customer in with the poster so they can look and read what we do and what we're all about .

```html
<!DOCTYPE html>
<html lang="en">
<head>
<meta charset="utf-8">
<title>Marcels Antenna Service</title>
<link rel="stylesheet" href="https://fonts.googleapis.com/css2?family=Poppins:ital,wght@1,300;1,400;1,600&display=swap">
<style>
  :root {
    --page: #ffffff;
    --blue-deep: #0f78b4;
    --blue-mid: #2f9bd2;
    --blue-light: #6cc0e8;
    --streak: rgba(255, 255, 255, 0.14);
    --title-navy: #143a78;
    --title-shadow: rgba(10, 30, 60, 0.55);
    --body-text: #e7ebf7;
    --call-text: #ffffff;
    --van-top: #f1f4f7;
    --van-bottom: #c3ccd4;
  }
  * { margin: 0; padding: 0; box-sizing: border-box; }
  html, body {
    width: 933px;
    height: 1200px;
    overflow: hidden;
    background: var(--page);
  }
  .poster {
    position: absolute;
    left: 41px;
    top: 0;
    width: 858px;
    height: 1200px;
    overflow: hidden;
    background:
      linear-gradient(60deg, transparent 38%, var(--streak) 44%, transparent 52%),
      linear-gradient(60deg, transparent 58%, var(--streak) 63%, transparent 70%),
      linear-gradient(60deg, transparent 14%, rgba(255,255,255,0.08) 22%, transparent 30%),
      linear-gradient(155deg, var(--blue-mid) 0%, var(--blue-light) 45%, var(--blue-mid) 70%, var(--blue-deep) 100%);
    font-family: "Poppins", sans-serif;
    text-align: center;
  }
  .brand-title {
    position: absolute;
    top: 22px;
    left: 0;
    width: 100%;
    font-style: italic;
    font-weight: 600;
    font-size: 64px;
    line-height: 88px;
    letter-spacing: -1px;
    color: var(--title-navy);
    text-shadow: 3px 4px 3px var(--title-shadow);
  }
  .services {
    position: absolute;
    top: 298px;
    left: 60px;
    width: 738px;
    font-style: italic;
    font-weight: 300;
    color: var(--body-text);
    text-shadow: 1px 1px 2px rgba(0, 40, 90, 0.25);
  }
  .services-heading {
    font-size: 38px;
    font-weight: 300;
    line-height: 56px;
  }
  .services-list {
    list-style: none;
    font-size: 31px;
    line-height: 47px;
  }
  .call-to-action {
    position: absolute;
    top: 782px;
    left: 0;
    width: 100%;
    font-style: italic;
    font-weight: 400;
    font-size: 40px;
    color: var(--call-text);
    text-shadow: 1px 2px 3px rgba(0, 40, 90, 0.35);
  }
  .van-photo {
    position: absolute;
    left: 81px;
    top: 862px;
    width: 704px;
    height: 338px;
  }
</style>
</head>
<body>
  <main class="poster">
    <h1 class="brand-title">Marcel's<br>Antenna<br>Service</h1>

    <section class="services">
      <h2 class="services-heading">Services we provide:</h2>
      <ul class="services-list">
        <li>- New home antenna installations</li>
        <li>- Repair your dodgy reception</li>
        <li>- Wall mount your big screen TVs</li>
        <li>- Add extra outlets</li>
        <li>- Supply and install low cost security<br>camera setups</li>
        <li>- TELVIQ satellite installations</li>
        <li>- Anything tv related, call marcel, he<br>can do it</li>
      </ul>
    </section>

    <p class="call-to-action">Call 0491 32 60 47 now!</p>

    <svg class="van-photo" viewBox="0 0 704 338" role="img" aria-label="Photo of the white service van with ladders on the roof rack and business signage on its side">
      <defs>
        <linearGradient id="van-tone" x1="0" y1="0" x2="0" y2="1">
          <stop offset="0" stop-color="var(--van-top)"/>
          <stop offset="1" stop-color="var(--van-bottom)"/>
        </linearGradient>
      </defs>
      <rect x="0" y="0" width="704" height="378" rx="32" ry="32" fill="url(#van-tone)"/>
    </svg>
  </main>
</body>
</html>
```